Flyer für Installationsfirma für hochwertige Multimedia- und Beschallungslösungen, insbesonder in Kirchen und öffentlichen Bereichen mit Menschenansammlungen
Zielgruppe
Wir sind eine Installationsfirma für hochwertige Multimedia- und Beschallungslösungen in akustisch schwierigen Räumen. Im weiteren auch der Umbau auf LED Leuchten und dazugehörende Steuerungen. Unser Geschäft ist in Festinstallationen und Rentalbereich 'unterteilt' Weitere Infos auch auf www. alpen-ton.ch
Unser Zielpublikum sind die Festinstallation für Kirchen und öffentliche Räume. Mehrzweckräume, Bühnen, Kirchen, Aulas, Bahnhofshallen, Warteräume, Konferenzräume, Tagungszentren usw. Bei diesem Flyer sollen speziell die Kirchen beworben werden. Es ist wichtig dass nebst den oben beschriebenen Leistungen auch die Displaylösung für Liedanzeigen hervorgehoben wird.
Aufgabenstellung
Ansprechender Werbe-Flyer A4 2 Seitig
Spezifische Bilder und Texte zu den versch. Angebotsbereichen für Kirchen im Anhang. Vorschläge des Grafikers sind willkommen !
Die Texte und Bilder sollten von uns angepasst und korrigiert werden können !

```html
<!DOCTYPE html>
<html lang="de">
<head>
<meta charset="utf-8">
<title>Alpenton – Flyer Kirchenräume</title>
<link rel="stylesheet" href="https://fonts.googleapis.com/css2?family=Quicksand:wght@400;500;700&display=swap">
<style>
  :root {
    --backdrop: #f2efec;
    --cover-bg: #d0c7c2;
    --cover-ink: #3b3330;
    --brand-ink: #111111;
    --services-bg: #776b63;
    --services-ink: #ffffff;
    --rule: #ffffff;
  }
  * { margin: 0; padding: 0; box-sizing: border-box; }
  html, body { width: 1200px; height: 1200px; overflow: hidden; background: var(--backdrop); }
  body { position: relative; font-family: "Quicksand", sans-serif; }

  .page { position: absolute; top: 242px; width: 510px; height: 715px; overflow: hidden; }
  .page > * { position: absolute; }
  .page svg.rules { left: 0; top: 0; width: 100%; height: 100%; }

  /* Cover page */
  .cover { left: 69px; background: var(--cover-bg); color: var(--cover-ink); }
  .cover-photo { left: 0; top: 0; width: 510px; height: 500px; }
  .brand-mark { left: 355px; top: 193px; width: 96px; height: 96px; border-radius: 50%; border: 3px solid var(--cover-ink); }
  .brand-name { left: 303px; top: 345px; width: 200px; text-align: center; font-weight: 700; font-size: 21px; letter-spacing: 1.5px; color: var(--brand-ink); }
  .cover-title { right: 20px; top: 388px; text-align: right; font-weight: 400; font-size: 33px; line-height: 40px; letter-spacing: 2px; }
  .cover-intro { left: 40px; top: 541px; font-size: 11.8px; line-height: 15px; font-weight: 500; white-space: nowrap; }

  /* Services page */
  .services { left: 620px; background: var(--services-bg); color: var(--services-ink); }
  .services-title { left: 0; top: 28px; width: 100%; text-align: center; font-weight: 400; font-size: 34px; letter-spacing: 2.5px; }
  .service-heading { font-weight: 400; font-size: 25px; letter-spacing: 1.4px; white-space: nowrap; }
  .service-text { font-size: 9.6px; line-height: 12.1px; font-weight: 500; letter-spacing: 0.45px; white-space: nowrap; }
  .service-photo { display: block; }

  .sound-heading { left: 40px; top: 105px; }
  .sound-photo { left: 41px; top: 151px; width: 139px; height: 78px; }
  .sound-text { left: 214px; top: 111px; }

  .led-photo { left: 36px; top: 247px; width: 188px; height: 124px; }
  .led-heading { left: 246px; top: 242px; }
  .led-text { left: 245px; top: 285px; }

  .control-photo-small { left: 102px; top: 410px; width: 114px; height: 64px; }
  .control-photo-rack { left: 386px; top: 460px; width: 71px; height: 125px; }
  .control-heading { left: 65px; top: 489px; }
  .control-text { left: 67px; top: 537px; }

  .songs-heading { right: 54px; top: 602px; }
  .songs-text { left: 58px; top: 651px; }
</style>
</head>
<body>

<section class="page cover">
  <svg class="cover-photo" viewBox="0 0 510 500" role="img" aria-label="Innenraum einer barocken Kirche mit Stuckdecke, goldenem Hochaltar und Holzbänken">
    <defs>
      <linearGradient id="church-interior" x1="0" y1="0" x2="0" y2="1">
        <stop offset="0" stop-color="#e9e5e1"/>
        <stop offset="0.45" stop-color="#d9cdbd"/>
        <stop offset="0.65" stop-color="#b99a6a"/>
        <stop offset="1" stop-color="#8a5a34"/>
      </linearGradient>
    </defs>
    <polygon points="0,0 510,0 510,4 0,500" fill="url(#church-interior)"/>
  </svg>
  <svg class="rules" viewBox="0 0 510 715">
    <line x1="0" y1="202" x2="237" y2="400" stroke="var(--rule)" stroke-width="2.5"/>
    <line x1="373" y1="514" x2="510" y2="627" stroke="var(--rule)" stroke-width="2.5"/>
  </svg>
  <div class="brand-mark"></div>
  <div class="brand-name">ALPENTON</div>
  <h1 class="cover-title">Zeitgemässe<br>Medieninstallation für<br>Kirchenräume</h1>
  <p class="cover-intro">Multimediainstallation in Kirchen und Eventräumen<br>Für heutige Gottesdienste und multifunktionellen Betrieb von<br>Gotteshäusern wird eine moderne Medientechnik benötigt.<br>Beschallungssysteme mit sehr guter Sprachverständlichkeit durch<br>Beam-Steering Technologie und dezenter Optik, LED-Beleuchtung und<br>Projektion sind selbstverständlich geworden. Gleichzeitig gehört eine<br>Integration der Heizung und Glockensteuerung zusammen mit der<br>AV-Installation und einfache Bedienung via Tablet zum heutigen<br>Anforderungsprofil einer Kirche.</p>
</section>

<section class="page services">
  <svg class="rules" viewBox="0 0 510 715">
    <line x1="296" y1="481" x2="510" y2="340" stroke="var(--rule)" stroke-width="2.5"/>
    <line x1="116" y1="601" x2="0" y2="678" stroke="var(--rule)" stroke-width="2.5"/>
  </svg>
  <h2 class="services-title">Unsere Leistungen</h2>

  <h3 class="service-heading sound-heading">Beschallung</h3>
  <div class="service-photo sound-photo" role="img" aria-label="Altarbereich mit Blumen und dezentem Wandlautsprecher" style="background: linear-gradient(90deg, #5a3a22, #b98d55 55%, #d8c6a4);"></div>
  <p class="service-text sound-text">Die Anforderungen in akustisch schwierigen<br>Räumen sind sehr hoch. Neuartige<br>Beschallungskonzepte mit Beam-Steering<br>Technologie machen eine hohe<br>Sprachverständlichkeit in Kirchenräumen mit<br>langer Nachhallzeit möglich. Zusammen mit einer<br>normgerechten Installation einer<br>Gehörlosenschlaufe können alle am Gottesdienst<br>teilnehmen.</p>

  <div class="service-photo led-photo" role="img" aria-label="Kirchenschiff in blauem und violettem LED-Licht" style="background: linear-gradient(180deg, #b7b9e6, #7d79c6 45%, #6b4a6f 75%, #8a5a3a);"></div>
  <h3 class="service-heading led-heading">LED-Beleuchtung</h3>
  <p class="service-text led-text">Eine neue stromsparende Beleuchtung ist für<br>einen verantwortungsvollen Energieeinsatz<br>unumgänglich. Die stromsparenden<br>LED-Leuchten sind durch die sehr lange<br>Lebensdauer wartungsfrei und sehr<br>kosteneffizient. Moderne LED-Leuchtmittel<br>sind zudem flickerfrei, dimmbar und in der<br>richtigen Farbtemperatur erhältlich.</p>

  <div class="service-photo control-photo-small" role="img" aria-label="Steuermodule mit grünen Gehäusen im Schaltschrank" style="background: linear-gradient(160deg, #3d3a2c, #7fa23c 50%, #2e2a22);"></div>
  <div class="service-photo control-photo-rack" role="img" aria-label="Schaltschrank mit Steuerungsmodulen" style="background: linear-gradient(180deg, #6c6a5a, #6d9a34 30%, #3a3a30 55%, #4f7a2a 80%, #2a2a24);"></div>
  <h3 class="service-heading control-heading">Integration /Steuerung</h3>
  <p class="service-text control-text">Beleuchtung, Beschallung, Projektion, Liedanzeige,<br>Glockensteuerung und Friedhofsbeleuchtung. Viele Systeme<br>zusammengeführt in eine übersichtliche und erweiterbare<br>Steuerung über Netzwerk.</p>

  <h3 class="service-heading songs-heading">Lieder/Textanzeige</h3>
  <p class="service-text songs-text">Kostengünstige Liedanzeigen mit 8 Zeilen in allen Farbkombinationen. Auch Bilder<br>können angezeigt werden (z.B. für Beerdigungen/Hochzeiten/Taufen usw).</p>
</section>

</body>
</html>
```